Ned Walcott Fairway Lessons Rack Card

The flyer will be a rack card. Front side only. Nothing on back. 3.75 inches by 8.5 inches. Or close to that. I’d like it to be as colorful as possible and to include several logos in different places.
The brochure is to attract golfers attention and still look traditional and classy not crazy or to artsy. Golf is a very traditional sport and would just like it to look professional and welcoming so golfers no I’m credible in my teaching and they will learn something. I will send a rough idea and a sample of one I had before but use your creative skills and ingenuity to design it. You will have to put my name: Ned Walcott under the TLQ logo. It is a requirement by the TLQ. Also the logo size must me .0875 inches high. If possible use a gotham or Hoefler text type or something businesslike or similar for my name. Also I am sorry for the different logos available on this file because I am not tech savvy so you will have to choose the best logo and cut it out of the grouping to match what you want to do. I am sorry for all the details. I will be available all weekend if you need more info. or help. I am sure you are very skilled and can tell I am not. Sorry. I laid out a sketch for you so you know what info. verbiage is important. and where to somewhat place the logos. Up to your skill for most of it. Your design! Go for it.!

Target Market(s)

Golfers of all ages from 18-70. Men and Women.

Industry/Entity Type

Golf Industry. Teaching and learning game if golf

Font styles to use
Sans Serif
Other font styles liked:
• Mixture maybe traditional type. Easy to read.

Colors

Designer to choose only greyscale colors for use in the design.

Requirements
Must have
• My JPG golf logo and the TLQ official logo. Also will send several other logos to put in. I will tell you where they should go on the rack card.
Nice to have
• Maybe a golf picture from a course with a green and flag as the one on my old brochure I’m sending or similar. It just adds color and eye catching
Should not have
• Nothing hard to read or difficult to comprehend. Pretty straight forward and quality and style in a traditional sense,

```html
<!DOCTYPE html>
<html lang="en">
<head>
<meta charset="utf-8">
<title>Ned Walcott Fairway Lessons Rack Card</title>
<link rel="stylesheet" href="https://fonts.googleapis.com/css2?family=Montserrat:wght@400;500;600;700;800&family=Cormorant+Garamond:wght@500&display=swap">
<style>
:root{
  --page:#c9c9c9;
  --paper:#ffffff;
  --ink:#2a2b30;
  --dark:#2b2c33;
  --mid:#5e5f64;
  --grey:#a9aaae;
  --light:#c4c5c8;
  --footer:#5b5c61;
}
*{margin:0;padding:0;box-sizing:border-box}
html,body{width:832px;height:1200px;overflow:hidden;background:var(--page)}
body{font-family:'Montserrat',sans-serif;color:var(--ink)}
.card{position:absolute;left:151px;top:0;width:530px;height:1200px;background:var(--paper);overflow:hidden}
.card-shapes{position:absolute;left:0;top:0}
.abs{position:absolute}
.brand-name{left:0;width:530px;top:62px;text-align:center;font-family:'Cormorant Garamond',serif;font-weight:500;font-size:33px;line-height:1.05;color:#8e8f93}
.brand-url{left:0;width:530px;top:152px;text-align:center;font-weight:600;font-size:13px;letter-spacing:.4px;color:var(--ink)}
.headline{left:0;width:530px;top:532px;text-align:center;font-weight:800;font-size:32.5px;color:#fff;letter-spacing:.2px}
.price{top:592px;width:150px;text-align:center;font-weight:700;font-size:27px;color:#fff}
.price sup{font-size:14px;text-decoration:underline;vertical-align:11px;margin-left:4px}
.price-label{top:639px;width:150px;text-align:center;font-weight:600;font-size:11.5px;line-height:16px;color:var(--ink);letter-spacing:.3px}
.includes-tag{left:40px;top:695px;width:21px;height:95px;border-radius:11px;background:var(--grey);color:#fff;font-weight:700;font-size:11px;letter-spacing:1px;writing-mode:vertical-rl;transform:rotate(180deg);text-align:center;line-height:21px}
.features{left:68px;top:690px;list-style:none;color:#fff;font-size:12.6px;line-height:21.5px}
.features li{display:flex;gap:6px}
.features svg{flex:none;margin-top:6px}
.features .wrap{line-height:16px;margin-top:3px}
.info-box{left:310px;top:692px;width:182px;height:97px;border:2px solid #fff;border-radius:12px;overflow:hidden}
.info-top{height:46px;background:var(--grey);color:#fff;font-size:13px;line-height:17px;text-align:center;padding-top:6px;border-bottom:2px solid #fff}
.info-bottom{color:#fff;font-size:12.5px;text-align:center;padding-top:6px;line-height:17px}
.info-bottom b{font-size:11px;font-weight:700;letter-spacing:.2px}
.partner{top:854px;font-weight:800;font-size:30px;letter-spacing:-.5px}
.partner-a{left:78px;color:var(--light)}
.partner-b{left:300px;color:var(--dark)}
.package-title{left:0;width:530px;top:897px;text-align:center;font-weight:800;font-size:22.5px;color:var(--grey)}
.pkg-label{top:933px;width:200px;text-align:center;font-weight:600;font-size:11.5px;letter-spacing:.4px}
.pkg-pill{top:958px;width:124px;height:25px;border-radius:13px;background:var(--grey);color:#fff;font-weight:700;font-size:15px;text-align:center;line-height:25px}
.pkg-pill sup{font-size:8px;vertical-align:6px}
.pkg-divider{left:287px;top:934px;width:2px;height:46px;background:var(--ink)}
.pkg-includes{left:25px;top:992px;width:490px;font-size:12.4px;line-height:17px;color:var(--ink)}
.pkg-includes b{font-weight:700}
.tick{color:var(--grey);font-size:10px}
.badge{border-radius:50%}
.badge-guarantee{left:99px;top:1044px;width:73px;height:73px;background:var(--dark);border:3px solid var(--grey)}
.badge-member{left:230px;top:1042px;width:70px;height:70px;background:var(--grey);border:3px solid var(--dark)}
.badge-name{left:200px;width:130px;top:1119px;text-align:center;font-size:9px;font-weight:600}
.pro-credit{left:360px;top:1048px;font-size:12.6px;line-height:16.6px;color:var(--ink)}
.pro-credit b{font-weight:700}
.contact{top:1162px;color:#fff;font-size:12.5px;font-weight:500;display:flex;align-items:center;gap:6px}
</style>
</head>
<body>
<div class="card">
  <svg class="card-shapes" width="530" height="1200" viewBox="0 0 530 1200">
    <defs>
      <linearGradient id="courseTone" x1="0" y1="0" x2="0" y2="1">
        <stop offset="0" stop-color="#e2e2e2"/>
        <stop offset=".45" stop-color="#b9b9b9"/>
        <stop offset=".6" stop-color="#5a5a5a"/>
        <stop offset="1" stop-color="#8a8a8a"/>
      </linearGradient>
    </defs>
    <!-- top rim of photo area -->
    <path d="M0 210 Q265 170 530 210 L530 225 Q265 185 0 225Z" fill="var(--light)"/>
    <!-- course photo placeholder -->
    <path d="M0 222 Q265 182 530 222 L530 480 Q265 515 0 480Z" fill="url(#courseTone)" role="img" aria-label="Black and white photo of a golf ball on a tee in the grass, with a bag of clubs and a flagstick on the green behind"/>
    <!-- dark offer panel -->
    <path d="M0 478 Q265 512 530 478 L530 490 Q265 525 0 490Z" fill="var(--light)"/>
    <path d="M0 489 Q265 523 530 489 L530 860 L0 860Z" fill="var(--dark)"/>
    <path d="M0 797 Q265 848 530 797 L530 870 L0 870Z" fill="var(--light)"/>
    <path d="M0 806 Q265 857 530 806 L530 880 L0 880Z" fill="var(--paper)"/>
    <!-- price box -->
    <rect x="115" y="588" width="300" height="86" rx="8" fill="var(--grey)"/>
    <rect x="265" y="588" width="150" height="47" fill="#c0c0c3"/>
    <path d="M265 588 H407 a8 8 0 0 1 8 8 V635 H265Z" fill="#b3b4b8"/>
    <rect x="115" y="635" width="300" height="39" fill="var(--paper)"/>
    <rect x="265" y="635" width="150" height="39" fill="#f0f0f0"/>
    <!-- footer band -->
    <path d="M0 1120 Q265 1150 530 1120 L530 1200 L0 1200Z" fill="var(--grey)"/>
    <path d="M0 1130 Q265 1160 530 1130 L530 1200 L0 1200Z" fill="var(--footer)"/>
  </svg>

  <div class="abs brand-name">Ned Walcott<br>Fairway Lessons</div>
  <div class="abs brand-url">WWW.NEDWALCOTTLESSONS.COM</div>

  <h1 class="abs headline">GOLF SWING ANALYSIS</h1>
  <div class="abs price" style="left:115px">$59<sup>99</sup></div>
  <div class="abs price" style="left:265px">$79<sup>00</sup></div>
  <div class="abs price-label" style="left:115px">1 - HOUR<br>ANALYSIS</div>
  <div class="abs price-label" style="left:265px">ONE TIME<br>LIMITED OFFER</div>

  <div class="abs includes-tag">INCLUDES</div>
  <ul class="abs features">
    <li><svg width="9" height="9" viewBox="0 0 10 10"><path d="M1 5 L4 8 L9 1" stroke="#c4c5c8" stroke-width="2" fill="none"/></svg>Swing Analysis w/Video</li>
    <li><svg width="9" height="9" viewBox="0 0 10 10"><path d="M1 5 L4 8 L9 1" stroke="#c4c5c8" stroke-width="2" fill="none"/></svg>Review Of Swing Technique</li>
    <li><svg width="9" height="9" viewBox="0 0 10 10"><path d="M1 5 L4 8 L9 1" stroke="#c4c5c8" stroke-width="2" fill="none"/></svg>Suggested Tips &amp; Drills</li>
    <li><svg width="9" height="9" viewBox="0 0 10 10"><path d="M1 5 L4 8 L9 1" stroke="#c4c5c8" stroke-width="2" fill="none"/></svg><span class="wrap">Video and Summary sent to<br>your mobile devices</span></li>
  </ul>
  <div class="abs info-box">
    <div class="info-top">Beginners<br>to Advanced</div>
    <div class="info-bottom">Additional Info @<br><b>WWW.NWALCOTT.COM</b></div>
  </div>

  <div class="abs partner partner-a">Swingtrak</div>
  <div class="abs partner partner-b">Launchly</div>

  <div class="abs package-title">SPECIAL LESS ON PACKAGE</div>
  <div class="abs pkg-label" style="left:82px">3-ONE HOUR LESSONS</div>
  <div class="abs pkg-label" style="left:269px">(LIMITED DEAL)</div>
  <div class="abs pkg-divider"></div>
  <div class="abs pkg-pill" style="left:120px">REG <sup>$</sup>237<sup>00</sup></div>
  <div class="abs pkg-pill" style="left:307px">REG <sup>$</sup>225<sup>00</sup></div>
  <p class="abs pkg-includes"><b>INCLUDES :</b> <span class="tick">✔</span> Video Analysis <span class="tick">✔</span> Lesson Summary And Video Review Sent To Mobile Devices <span class="tick">✔</span> Tips And Drills <span class="tick">✔</span> Action Plan To Improve</p>

  <div class="abs badge badge-guarantee" aria-label="Satisfaction guarantee badge"></div>
  <div class="abs badge badge-member" aria-label="TLQ member badge"></div>
  <div class="abs badge-name">Ned Walcott</div>
  <div class="abs pro-credit"><b>Ned Walcott</b><br>Class A Member<br>GSC <span class="tick">✔</span> Century<br>Member TLQ</div>

  <div class="abs contact" style="left:26px">
    <svg width="16" height="11" viewBox="0 0 16 11"><rect width="16" height="11" rx="1" fill="#fff"/><path d="M1 1 L8 6 L15 1" stroke="#5b5c61" stroke-width="1.5" fill="none"/></svg>nwalcott@fairwaymail.com
  </div>
  <div class="abs contact" style="left:220px">
    <svg width="12" height="12" viewBox="0 0 24 24"><path fill="#fff" d="M6.6 10.8a15 15 0 0 0 6.6 6.6l2.2-2.2a1 1 0 0 1 1-.25 11.4 11.4 0 0 0 3.6.57 1 1 0 0 1 1 1V20a1 1 0 0 1-1 1A17 17 0 0 1 3 4a1 1 0 0 1 1-1h3.5a1 1 0 0 1 1 1c0 1.25.2 2.45.57 3.57a1 1 0 0 1-.25 1z"/></svg>555-014-2276
  </div>
  <div class="abs contact" style="left:362px">
    <svg width="12" height="12" viewBox="0 0 24 24" fill="none" stroke="#fff" stroke-width="2"><circle cx="12" cy="12" r="10"/><path d="M2 12h20M12 2a15 15 0 0 1 0 20M12 2a15 15 0 0 0 0 20"/></svg>nwalcott.com
  </div>
</div>
</body>
</html>
```